Brindle Chill Supplies Stationery Design

Stationery Design

Thank you to all those who have submitted the logos. We have selected the logo for our new identity and we are now looking for stationery ideas.

The attached logo must be used in all stationery designs.

We require the following items of stationery:

1. Business Cards for 10 employees – Double Sided – All the card will have the same address:

7 – 31 Marrowby Lane, Kingston Upon Thames, Surrey, KT4 9QX, United Kingdom

Office phone number: +44 (0)208 613 7742

Freephone: 0800 129 4837

Fax: +44 (0)20 8731 2964

Website: www.brindlechill.example

The names on the cards and mobile numbers – will be given on selection of final design.

A few of the cards will have different emails but 5/6 card will have the same email address.

2. Letterhead A4 – same contact details as above – email address to be used info@brindlechill.example

3. Compliments Slip – same details as no.2

4. Envelope designs – with just the address, Freephone and Website.

Sizes Required: C4 – 324mm x 229mm – Windows and Regular

DL – 110mm x 220mm – Windows and Regular

5. A4 Ring Binder – Logo at the front and back and side; company name on the front and side of the binder (Brindle Chill Supplies); contact details at the back; same as number 2 above.

The ring binder will have food, drink and hygiene inserts inside and will act as a temporary brochure.

It may help with the design process to know we sell a range of frozen food products including chips, burgers, fish, frozen poultry items, vegetables, ice cream, desserts, bakery products, pies, pasties, onion rings, pizza toppings etc.

We also sell ambient products such as sauces, crisps such as dunmores, chocolates such as Hollensby, Vorelle, Quib etc.

Drinks wise we sell branded products such as zesta tonic, fizmo, lumra, glint, sky hare etc; As well as juices and mineral water.

We also sell hygiene products such as tissue paper, hand towels, and other washroom products, bleaches etc.

Our website doesn’t have the full range of products but gives you a good idea of what we do www.brindlechill.example

Please note we are looking for a classy, slick design so don’t worry about trying to add all the products on the binder design; these have just been given to assist with the design process.

We may add a slogan to the stationery but the final decision on this still has to be taken and the profile will be updated within the next 72 hours.

This project will only last a maximum of 10-14 days, we don’t want to drag it out like the logo so please only submit creative ideas; which have been given thought in terms of design, text and graphics.

Any questions, feel free to ask.

Thank you and we look forward to your designs.

Regards

Torvin Ashcombe

I've uploaded an Adobe Illustrator CS2.ai file, and an EPS file of my new logo so you can get better clarity within your designs for this project

Thanks
Torvin

Hi

We have had various questions in respect of dimensions and budget; we have addressed both issues below by providing dimensions and we will be increasing the budget to $500 as soon as Pixel Bazaar let us know how we can increase; they have already been emailed.

In respect of the dimensions, we have had various answers but here are the most common sizes.

 

There are various sizes of lever arch A4 folders but the most common ones are below:

 

 

• Dimensions width 28.5cm, height 32cm,spine 9cm
• Dimensions (mm)H:315 x W:285
• Dimensions (mm) H:31cm x W:27cm

 

The most common thickness in the UK seems to be 70mm; so can we use this as a guide please.

 

 

Compliment Slip Sizes:

 

• Our Compliment Slips are DL in size. You should design your Compliment Slip to DL dimension but also add a 3mm bleed around each edge.

 

Trim Size – 99mm x 210mm

 

With Bleed – 105mm – 216mm

 

 

Business Cards:

 

Trim Size: 85mm x 55mm

 

With Bleed: 91mm x 61mm

 

 

We have extended the time frame and the budget on this so look forward to new designs.

 

I hope this helps and all the best for Christmas and 2010..

 

Regards

Torvin Ashcombe.

Hi Guys

Another important point to mention as each country has different rules...

In the Uk the postage stamps go in the top right hand corner of the envelope so we will have to have our logo company details etc in either the top left or the bottom of the envelope.

Also all envelopes must have at the back our return address:

Return Address:

Brindle Chill Supplies Ltd
7 - 31 Marrowby Lane
Ashvale Upon Wend
Wexshire
KT4 9QX

So we could even have the business logo, name and website address at the front and the address at the back.

Regards

Torvin

```html
<!DOCTYPE html>
<html lang="en">
<head>
<meta charset="utf-8">
<title>Brindle Chill Supplies – Business Card Options</title>
<link rel="stylesheet" href="https://fonts.googleapis.com/css2?family=Montserrat:wght@700&family=PT+Sans:ital,wght@0,400;0,700;1,400&display=swap">
<style>
  :root {
    --backdrop: #5b3722;
    --navy: #1b2b7c;
    --navy-light: #3452b0;
    --red: #b5141d;
    --red-light: #d6434a;
    --white: #ffffff;
    --ink: #3a3a3a;
    --grey: #9a9a9a;
    --heading: #f4ece4;
  }
  * { margin: 0; padding: 0; box-sizing: border-box; }
  html, body { width: 1200px; height: 960px; overflow: hidden; }
  body {
    background: var(--backdrop);
    font-family: "PT Sans", Arial, sans-serif;
    position: relative;
  }
  .section-heading {
    position: absolute;
    top: 40px;
    font-family: "Montserrat", Arial, sans-serif;
    font-weight: 700;
    font-size: 27px;
    letter-spacing: 5px;
    color: var(--heading);
  }
  .section-heading--front { left: 120px; }
  .section-heading--back { left: 700px; }

  .card {
    position: absolute;
    overflow: hidden;
    box-shadow: 4px 6px 14px rgba(0,0,0,0.45);
  }
  .card--front { width: 512px; height: 330px; left: 48px; }
  .card--back { width: 556px; height: 334px; left: 600px; background: var(--white); }
  .card--row1 { top: 139px; }
  .card--row2 { top: 523px; }
  .card--blue { background: var(--navy); }
  .card--red { background: var(--red); }

  .swirl-area {
    position: absolute;
    left: 0; top: 0;
    width: 380px; height: 280px;
  }
  .card--blue .swirl-area {
    background: radial-gradient(ellipse at 42% 40%, var(--navy-light) 0%, rgba(52,82,176,0.55) 45%, rgba(27,43,124,0) 72%);
  }
  .card--red .swirl-area {
    background: radial-gradient(ellipse at 42% 40%, var(--red-light) 0%, rgba(214,67,74,0.5) 45%, rgba(181,20,29,0) 72%);
  }

  .lockup {
    position: absolute;
    display: flex;
    align-items: center;
    gap: 10px;
    font-weight: 700;
    white-space: nowrap;
  }
  .lockup__mark { border-radius: 50%; flex: none; }
  .lockup--front { right: 26px; bottom: 30px; color: var(--white); font-size: 17px; }
  .lockup--front .lockup__mark { width: 26px; height: 26px; background: var(--white); }
  .lockup--back { font-size: 22px; color: var(--navy); }
  .lockup--back .lockup__mark { width: 54px; height: 54px; background: var(--red); }
  .card--row1 .lockup--back { left: 20px; top: 40px; }
  .card--row2 .lockup--back { right: 20px; top: 40px; }

  .holder {
    position: absolute;
    font-size: 17px;
    line-height: 1.25;
  }
  .holder__name { font-weight: 700; font-variant: small-caps; letter-spacing: 1px; font-size: 19px; }
  .holder__role { font-style: italic; color: var(--grey); }
  .card--row1 .holder { right: 30px; top: 52px; text-align: left; }
  .card--row1 .holder__name { color: var(--navy); }
  .card--row2 .holder { left: 30px; top: 50px; }
  .card--row2 .holder__name { color: var(--red); }

  .contact-band {
    position: absolute;
    left: 0; top: 176px;
    width: 556px; height: 106px;
  }
  .contact-band svg { position: absolute; left: 0; top: 0; }
  .phones, .address {
    position: absolute;
    top: 14px;
    font-size: 15px;
    line-height: 1.45;
  }
  .phones { left: 28px; }
  .phones b { display: inline-block; width: 22px; }
  .address { right: 18px; text-align: right; color: var(--white); }
  .card--row1 .phones { color: var(--white); }
  .card--row2 .phones { color: var(--ink); }

  .web {
    position: absolute;
    left: 270px;
    width: 286px;
    top: 290px;
    text-align: center;
    font-size: 15px;
    line-height: 1.2;
  }
  .card--row1 .web { color: var(--navy); }
  .card--row2 .web { color: var(--red); }
  .web__freephone { letter-spacing: 2px; }
</style>
</head>
<body>
  <h2 class="section-heading section-heading--front">SIDE 1 OPTIONS</h2>
  <h2 class="section-heading section-heading--back">SIDE 2 OPTIONS</h2>

  <section class="card card--front card--blue card--row1">
    <div class="swirl-area" role="img" aria-label="Large pale blue swirl of petal shapes from the brand symbol"></div>
    <div class="lockup lockup--front"><span class="lockup__mark"></span>Brindle Chill Supplies</div>
  </section>

  <section class="card card--back card--row1">
    <div class="lockup lockup--back"><span class="lockup__mark"></span>Brindle Chill Supplies</div>
    <div class="holder">
      <p class="holder__name">John Doe</p>
      <p class="holder__role">Designation</p>
    </div>
    <div class="contact-band">
      <svg width="556" height="106" viewBox="0 0 556 106">
        <polygon points="0,0 300,0 266,106 0,106" fill="var(--navy)"/>
        <polygon points="310,0 556,0 556,106 276,106" fill="var(--red)"/>
      </svg>
      <p class="phones">
        <b>t:</b> +44 (0)208 613 7742<br>
        <b>f:</b> +44 (0)20 8731 2964<br>
        <b>m:</b> number goes in here
      </p>
      <p class="address">
        7 – 31 Marrowby Lane<br>
        Ashvale Upon Wend, Wexshire<br>
        KT4 9QX, United Kingdom
      </p>
    </div>
    <p class="web">www.brindlechill.example<br><span class="web__freephone">0800 129 4837</span></p>
  </section>

  <section class="card card--front card--red card--row2">
    <div class="swirl-area" role="img" aria-label="Large pale red swirl of petal shapes from the brand symbol"></div>
    <div class="lockup lockup--front"><span class="lockup__mark"></span>Brindle Chill Supplies</div>
  </section>

  <section class="card card--back card--row2">
    <div class="holder">
      <p class="holder__name">John Doe</p>
      <p class="holder__role">Designation</p>
    </div>
    <div class="lockup lockup--back"><span class="lockup__mark"></span>Brindle Chill Supplies</div>
    <div class="contact-band">
      <svg width="556" height="106" viewBox="0 0 556 106">
        <polygon points="310,0 556,0 556,106 276,106" fill="var(--red)"/>
      </svg>
      <p class="phones">
        <b>t:</b> +44 (0)208 613 7742<br>
        <b>f:</b> +44 (0)20 8731 2964<br>
        <b>m:</b> number goes in here
      </p>
      <p class="address">
        7 – 31 Marrowby Lane<br>
        Ashvale Upon Wend, Wexshire<br>
        KT4 9QX, United Kingdom
      </p>
    </div>
    <p class="web">www.brindlechill.example<br><span class="web__freephone">0800 129 4837</span></p>
  </section>
</body>
</html>
```